Relaunch kelvorin.com

I need someone to review my existing site at WordPress, make it more contemporary and visually appealing while preserving the content, which is quite text-dense, and improve the navigation. For example, if you go to https://kelvorin.com/claims-handled/ you will see links to dedicated pages for various client groups - I would like those to somehow be evident from the home page.

It would be simpler to keep it at WordPress but I am open to using a different CMS if necessary.

Fluency in Spanish would be useful, since part of the site is in Spanish.

Target Market(s)

Shipowners, vessel operators, ship managers

Industry/Entity Type

Marine insurance / marine transportation

Number of Pages Required

5+ page

Colors

Designer to choose colors to be used in the design.

Requirements
Must have
• Substantially preserve exciting content, but make it more accessible.
Nice to have
• This is an online brochure - we don't sell anything on line. I would like the theme to tie in to the colors in the existing logo, which we will keep.

```html
<!DOCTYPE html>
<html lang="en">
<head>
<meta charset="utf-8">
<title>The Kelvorin Company — Average Adjusters and Marine Insurance Consultants</title>
<link href="https://fonts.googleapis.com/css2?family=Oswald:wght@400;500;600&family=Poppins:wght@400;500;600&display=swap" rel="stylesheet">
<style>
:root{
  --red:#b3291f;
  --red-dark:#8e1d15;
  --ink:#161616;
  --text:#555;
  --line:#cfcfcf;
  --white:#fff;
  --dark:#1e1e1e;
  --soft:#f4f4f4;
}
*{box-sizing:border-box;margin:0;padding:0}
html,body{width:1200px;height:3631px;overflow:hidden}
body{position:relative;background:var(--white);font-family:"Poppins",sans-serif;color:var(--text)}
.abs{position:absolute}
h1,h2,h3,.btn,.nav a,.brand-name{font-family:"Oswald",sans-serif}
.btn{display:inline-block;background:var(--red);color:var(--white);font-size:16px;font-weight:500;padding:11px 27px;text-decoration:none;outline:2px solid var(--red);outline-offset:3px}

/* header */
.site-header{top:0;left:0;width:1200px;height:82px;background:rgba(40,44,44,.55);z-index:5}
.brand{left:90px;top:14px;color:var(--white)}
.brand-name{font-size:34px;font-weight:500;letter-spacing:4px;line-height:1}
.brand-tag{font-size:9px;letter-spacing:4px;margin-top:4px;font-family:"Poppins",sans-serif}
.nav{right:92px;top:21px;display:flex;align-items:center;gap:35px}
.nav a{color:var(--white);text-decoration:none;font-size:15px}
.nav .track{background:var(--white);color:var(--ink);font-weight:500;padding:10px 15px}

/* hero */
.hero{top:0;left:0;width:1200px;height:870px;background:linear-gradient(100deg,#3a3d3a 0%,#5b5e56 40%,#6b5248 60%,#3b3533 85%,#2b2b2b 100%)}
.hero-title{left:90px;top:230px;color:var(--white);font-size:96px;font-weight:600;line-height:.93}
.hero-sub{left:90px;top:428px;color:var(--white);font-size:19px;font-weight:500;line-height:27px;width:400px;font-family:"Oswald",sans-serif}
.hero-btn{left:95px;top:511px}
.hero-edge{top:670px;left:0}

/* services */
.section-title{color:var(--ink);font-size:33px;font-weight:500;text-align:center}
.services-title{top:945px;left:0;width:1200px}
.services{top:1057px;left:151px;width:900px;height:208px;border:1px solid var(--line);display:flex}
.service{flex:1;position:relative;text-align:center;padding:62px 26px 0}
.service+.service{border-left:1px solid var(--line)}
.service h3{font-size:17px;font-weight:500;color:var(--ink);margin-bottom:8px}
.service p{font-size:12.5px;line-height:20px}
.service-icon{position:absolute;top:-52px;left:50%;margin-left:-50px;width:100px;height:100px;border-radius:50%;background:var(--white);border:1px solid var(--line);display:flex;align-items:center;justify-content:center}
.service-icon.active{background:var(--red);border-color:var(--red);outline:2px solid var(--red);outline-offset:3px}
.service-arrow{position:absolute;bottom:-19px;left:50%;margin-left:-23px;width:46px;height:38px;background:var(--red);display:flex;align-items:center;justify-content:center}
.services-btn{top:1318px;left:522px}

/* about */
.about{top:1451px;left:89px;width:1022px;height:351px;background:var(--white);box-shadow:0 20px 50px rgba(0,0,0,.08)}
.about-img{left:0;top:0;width:511px;height:351px;background:linear-gradient(180deg,#6b7477 0%,#40494d 45%,#2d3a3c 70%,#5c3330 100%)}
.about-body{left:550px;top:46px;width:420px}
.about-body h2{color:var(--ink);font-size:33px;font-weight:500;margin-bottom:18px}
.body-copy{font-size:12.5px;line-height:22.5px}
.about-body .btn{margin-top:26px}

/* qualifications */
.quals{top:1894px;left:0;width:1200px;height:286px;background:linear-gradient(90deg,#2c2c2c,#4a4a4a 50%,#2a2a2a)}
.quals-body{top:1960px;left:0;width:1200px;text-align:center;color:var(--white)}
.quals-body h2{font-size:33px;font-weight:500;margin-bottom:8px}
.quals-body p{font-size:12.5px;line-height:22px;width:680px;margin:0 auto 22px}

/* profession */
.prof-text{top:2306px;left:104px;width:420px}
.prof-text h2{color:var(--ink);font-size:33px;font-weight:500;line-height:40px;margin-bottom:12px}
.prof-text .btn{margin-top:26px}
.prof-frame{left:568px;top:2300px;width:510px;height:345px;background:var(--red)}
.prof-img{left:581px;top:2272px;width:511px;height:362px;background:linear-gradient(180deg,#3c4a54 0%,#5d6669 45%,#8a2a25 65%,#2c2f31 100%)}

/* map */
.map{top:2758px;left:0;width:1200px;height:520px;background:linear-gradient(135deg,#eceff1,#e3e7ea 50%,#eef0f2)}
.map-pin{left:543px;top:2903px;width:114px;height:114px;border-radius:50%;background:var(--red);display:flex;align-items:center;justify-content:center}

/* footer */
.footer{top:3095px;left:0}
.footer-brand{left:92px;top:3360px;color:var(--white);text-align:center}
.footer-brand .brand-name{font-size:44px}
.socials{left:110px;top:3441px;display:flex;gap:8px}
.socials span{width:42px;height:42px;border-radius:50%;background:#4a4a4a}
.socials span:first-child{background:var(--red)}
.f-col{top:3305px;color:var(--white)}
.f-col h3{font-size:26px;font-weight:400;margin-bottom:14px}
.f-links{list-style:none;font-size:12.5px;line-height:27px;font-weight:500}
.contact-item{display:flex;gap:10px;font-size:12.5px;line-height:18px;margin-bottom:16px}
.contact-item b{font-weight:600;display:block}
.newsletter p{font-size:12.5px;line-height:18px;margin-bottom:14px}
.news-field{width:260px;height:48px;background:var(--white);display:flex;align-items:center;justify-content:space-between;padding:0 16px;color:#666;font-size:12px}
.f-rule{left:90px;top:3576px;width:1020px;height:1px;background:#3d3d3d}
.copyright{left:0;top:3592px;width:1200px;text-align:center;color:var(--white);font-size:14px;font-weight:500}
.chat{left:1128px;top:3547px;width:48px;height:48px;border-radius:50%;background:var(--red)}
</style>
</head>
<body>

<div class="abs hero" role="img" aria-label="Red semi truck on a highway at dusk"></div>
<svg class="abs hero-edge" width="1200" height="210" viewBox="0 0 1200 210" aria-hidden="true">
  <polygon points="0,20 790,190 1200,14 1200,210 0,210" fill="#b3291f"/>
  <polygon points="0,30 790,200 1200,50 1200,210 0,210" fill="#fff"/>
</svg>

<header class="abs site-header">
  <div class="abs brand"><div class="brand-name">KELVORIN</div><div class="brand-tag">The Kelvorin Company</div></div>
  <nav class="abs nav">
    <a href="#">Home</a><a href="#">About Us</a><a href="#">Claims Handled</a><a href="#">Resources</a><a href="#">Contact</a><a class="track" href="#">Track Your Order</a>
  </nav>
</header>

<h1 class="abs hero-title">THE KELVORIN<br>COMPANY</h1>
<p class="abs hero-sub">AVERAGE ADJUSTERS AND MARINE INSURANCE CONSULTANTS</p>
<a class="abs btn hero-btn" href="#">Learn More</a>

<svg class="abs" style="top:800px;left:0" width="1200" height="600" aria-hidden="true">
  <polygon points="900,0 1200,0 1200,380" fill="#f5f5f5"/>
</svg>

<h2 class="abs section-title services-title">OUR SERVICES</h2>
<div class="abs services">
  <div class="service">
    <div class="service-icon">
      <svg width="52" height="52" viewBox="0 0 52 52" fill="none" stroke="#222" stroke-width="2"><rect x="4" y="6" width="44" height="40" rx="3"/><line x1="10" y1="17" x2="42" y2="17"/><rect x="12" y="13" width="8" height="8" fill="#fff"/><line x1="10" y1="27" x2="42" y2="27"/><rect x="30" y="23" width="8" height="8" fill="#fff"/><line x1="10" y1="37" x2="42" y2="37"/><rect x="18" y="33" width="8" height="8" fill="#fff"/></svg>
    </div>
    <h3>AVERAGE ADJUSTING</h3>
    <p>We specialize in average adjusting, the practice of dividing maritime risks proportionately among merchants involved in a voyage.</p>
    <div class="service-arrow"><svg width="18" height="18" viewBox="0 0 18 18" stroke="#fff" stroke-width="2" fill="none"><line x1="3" y1="15" x2="15" y2="3"/><polyline points="6,3 15,3 15,12"/></svg></div>
  </div>
  <div class="service">
    <div class="service-icon active">
      <svg width="54" height="54" viewBox="0 0 54 54" fill="none" stroke="#fff" stroke-width="2"><path d="M8 30h38l-5 10H13z"/><rect x="16" y="20" width="20" height="10"/><line x1="26" y1="10" x2="26" y2="20"/><path d="M6 46c4 3 8 3 12 0s8-3 12 0 8 3 12 0"/></svg>
    </div>
    <h3>MARINE INSURANCE CONSULTING</h3>
    <p>With extensive expertise in marine insurance, we provide consulting services that ensure our clients are well-prepared.</p>
    <div class="service-arrow"><svg width="18" height="18" viewBox="0 0 18 18" stroke="#fff" stroke-width="2" fill="none"><line x1="3" y1="15" x2="15" y2="3"/><polyline points="6,3 15,3 15,12"/></svg></div>
  </div>
  <div class="service">
    <div class="service-icon">
      <svg width="52" height="52" viewBox="0 0 52 52" fill="none" stroke="#222" stroke-width="2"><rect x="8" y="4" width="30" height="42"/><line x1="13" y1="12" x2="33" y2="12"/><line x1="13" y1="18" x2="33" y2="18"/><line x1="13" y1="24" x2="33" y2="24"/><circle cx="20" cy="35" r="5"/><path d="M44 8v32l-2 4-2-4V8z"/></svg>
    </div>
    <h3>CLAIMS HANDLING</h3>
    <p>Our claims handling services are tailored to various client groups, including ship owners, cargo owners, insurers, and legal professionals.</p>
    <div class="service-arrow"><svg width="18" height="18" viewBox="0 0 18 18" stroke="#fff" stroke-width="2" fill="none"><line x1="3" y1="15" x2="15" y2="3"/><polyline points="6,3 15,3 15,12"/></svg></div>
  </div>
</div>
<a class="abs btn services-btn" href="#">View All Services</a>

<section class="abs about">
  <div class="abs about-img" role="img" aria-label="Container ship loaded with cargo at port"></div>
  <div class="abs about-body">
    <h2>ABOUT US</h2>
    <p class="body-copy">Average" is believed to derive from an old Arabic word, "awar," meaning "damage." For centuries, average was a mechanism for dividing the risk inherent to a maritime adventure, with each merchant sharing in proportion to the profit, in the case of success, or in proportion to the value of what was saved, if the ship and goods had fallen into peril.</p>
    <a class="btn" href="#">Read More</a>
  </div>
</section>

<div class="abs quals" role="img" aria-label="Warehouse workers in safety vests, darkened"></div>
<div class="abs quals-body">
  <h2>IMPORTANCE OF QUALIFICATIONS</h2>
  <p>Because the profession remains self-regulated, be sure to verify an individual's professional qualifications when selecting an average adjuster.</p>
  <a class="btn" href="#">Read More</a>
</div>

<div class="abs prof-text">
  <h2>THE PROFESSION OF AVERAGE ADJUSTING</h2>
  <p class="body-copy">Average" is believed to derive from an old Arabic word, "awar," meaning "damage." For centuries, average was a mechanism for dividing the risk inherent to a maritime adventure, with each merchant sharing in proportion to the profit, in the case of success, or in proportion to the value of what was saved, if the ship and goods had fallen into peril.</p>
  <a class="btn" href="#">Learn More</a>
</div>
<div class="abs prof-frame"></div>
<div class="abs prof-img" role="img" aria-label="Red cargo truck parked on a waterfront under cloudy sky"></div>

<div class="abs map" role="img" aria-label="Street map showing the office location"></div>
<div class="abs map-pin">
  <svg width="34" height="44" viewBox="0 0 34 44"><path d="M17 2C9 2 3 8 3 16c0 11 14 26 14 26s14-15 14-26C31 8 25 2 17 2z" fill="#fff"/><circle cx="17" cy="16" r="5" fill="#b3291f"/></svg>
</div>

<svg class="abs footer" width="1200" height="536" viewBox="0 0 1200 536" role="img" aria-label="Dark footer backdrop with trucks at dusk">
  <defs><linearGradient id="footShade" x1="0" y1="0" x2="0" y2="1"><stop offset="0" stop-color="#2a2a2a"/><stop offset="1" stop-color="#151515"/></linearGradient></defs>
  <polygon points="0,138 410,0 1200,148 1200,536 0,536" fill="#b3291f"/>
  <polygon points="0,150 410,14 1200,160 1200,536 0,536" fill="url(#footShade)"/>
</svg>

<div class="abs footer-brand"><div class="brand-name">KELVORIN</div><div class="brand-tag">The Kelvorin Company</div></div>
<div class="abs socials" aria-label="Social profiles"><span></span><span></span><span></span><span></span></div>

<div class="abs f-col" style="left:379px">
  <h3>QUICK LINKS</h3>
  <ul class="f-links"><li>Home</li><li>About Us</li><li>Claims Handled</li><li>Resources</li><li>Contact</li></ul>
</div>

<div class="abs f-col" style="left:595px;width:230px">
  <h3>CONTACT INFO</h3>
  <div class="contact-item"><svg width="12" height="12" viewBox="0 0 12 12"><path d="M2 1l3 0 1 3-2 1c1 2 2 3 3 3l1-2 3 1v3c-6 0-10-4-9-9z" fill="#b3291f"/></svg><div><b>Phone*</b>+1 (555) 014-2290</div></div>
  <div class="contact-item"><svg width="12" height="12" viewBox="0 0 12 12"><rect x="0" y="2" width="12" height="8" fill="#b3291f"/><polyline points="0,2 6,7 12,2" stroke="#1e1e1e" fill="none"/></svg><div><b>Email*</b>info@kelvorin.com</div></div>
  <div class="contact-item"><svg width="12" height="12" viewBox="0 0 12 14"><path d="M6 0C3 0 1 2 1 5c0 4 5 9 5 9s5-5 5-9c0-3-2-5-5-5z" fill="#b3291f"/></svg><div><b>Location*</b>1180 Harbor Lane, Port Ellis, NY 10000, USA</div></div>
</div>

<div class="abs f-col newsletter" style="left:852px;width:260px">
  <h3>NEWSLETTER</h3>
  <p>Subscribe to our email address to get the latest news.</p>
  <div class="news-field"><span><svg width="11" height="9" viewBox="0 0 12 10"><rect width="12" height="10" fill="#b3291f"/></svg>&nbsp; Enter Your Email...</span><svg width="14" height="14" viewBox="0 0 14 14"><polygon points="0,6 14,0 9,14 7,8" fill="#b3291f"/></svg></div>
</div>

<div class="abs f-rule"></div>
<p class="abs copyright">Copyright © 2024 All Rights Reserved</p>
<div class="abs chat" aria-label="Chat"></div>

</body>
</html>
```